Investment fund letterhead + bus.card design

We are an investment fund focused on investments in the energy sector.
Pls. use design of existing logo in the attachment.
You are free to change the colors of the logo.
However, some associations should exist on the website as well.
webpage: www.brightelmholdings.fund.
This is a contest for a letterhead and business card. Therefore, pls. present letterhead and business card at once. The winner will be selected by January 11, 12pm.

Good luck! Good luck! Good luck! Good luck! Good luck! Good luck! Good luck! Good luck! Good luck! Good luck! Good luck! Good luck! Good luck! Good luck! Good luck! Good luck! Good luck! Good luck! Good luck! Good luck! Good luck! Good luck! Good luck! Good luck! Good luck! Good luck! Good luck! Good luck! Good luck! Good luck! Good luck! Good luck! Good luck! Good luck! Good luck! Good luck! Good luck! Good luck! Good luck! Good luck! Good luck! Good luck! Good luck! Good luck! Good luck! Good luck! Good luck! Good luck! Good luck! Good luck! Good luck! Good luck! Good luck! Good luck! Good luck! Good luck! Good luck! Good luck! Good luck! Good luck! Good luck! Good luck! Good luck! Good luck! Good luck! Good luck! Good luck! Good luck! Good luck! Good luck! Good luck! Good luck! Good luck! Good luck! Good luck! Good luck! Good luck! Good luck! Good luck! Good luck! Good luck! Good luck! Good luck! Good luck! Good luck! Good luck! Good luck! Good luck! Good luck! Good luck! Good luck! Good luck! Good luck! Good luck! Good luck! Good luck! Good luck! Good luck! Good luck! Good luck! Good luck! Good luck! Good luck! Good luck! Good luck! Good luck! Good luck! Good luck! Good luck! Good luck! Good luck! Good luck! Good luck! Good luck! Good luck! Good luck! Good luck! Good luck! Good luck! Good luck! Good luck! Good luck! Good luck! Good luck! Good luck! Good luck! Good luck! Good luck! Good luck! Good luck! Good luck! Good luck! Good luck! Good luck! Good luck! Good luck! Good luck! Good luck! Good luck! Good luck! Good luck! Good luck! Good luck! Good luck! Good luck! Good luck! Good luck! Good luck! Good luck! Good luck! Good luck! Good luck! Good luck! Good luck! Good luck! Good luck! Good luck! Good luck! Good luck! Good luck! Good luck! Good luck! Good luck! Good luck! Good luck! Good luck! Good luck! Good luck! Good luck! Good luck! Good luck! Good luck! Good luck! Good luck! Good luck! Good luck! Good luck! Good luck! Good luck! Good luck! Good luck! Good luck! Good luck! Good luck! Good luck! Good luck! Good luck! Good luck! Good luck! Good luck! Good luck! Good luck! Good luck! Good luck! Good luck! Good luck! Good luck! Good luck! Good luck! Good luck! Good luck! Good luck! Good luck! Good luck! Good luck! Good luck! Good luck! Good luck! Good luck! Good luck! Good luck! Good luck! Good luck! Good luck! Good luck! Good luck! Good luck! Good luck! Good luck! Good luck! Good luck! Good luck! Good luck! Good luck! Good luck! Good luck! Good luck! Good luck! Good luck! Good luck! Good luck! Good luck! Good luck! Good luck! Good luck! Good luck! Good luck! Good luck! Good luck! Good luck! Good luck! Good luck! Good luck!

Target Market(s)

Energy companies, Financial institutions

Industry/Entity Type

Investment Banking

Contact Information for Business Card

Title, Name, contacts

Font styles to use
Serif

Colors

Designer to choose colors to be used in the design.

Requirements
Must have
• Logo
Nice to have
• Some modern design hints/design elements.

```html
<!DOCTYPE html>
<html lang="en">
<head>
<meta charset="utf-8">
<title>Bright Elm Holdings — Letterhead and Business Cards</title>
<link rel="stylesheet" href="https://fonts.googleapis.com/css2?family=Arimo&family=Josefin+Sans:wght@600&family=Open+Sans:wght@400;600&display=swap">
<style>
  :root{
    --stage:#47484d;
    --orange:#f68b2a;
    --orange-deep:#ee7d1f;
    --brand:#f07d19;
    --paper:#ffffff;
    --ink:#2b2b2b;
    --muted:#555555;
    --rule:#bdbdbd;
    --ink-blue:#23307a;
  }
  *{margin:0;padding:0;box-sizing:border-box}
  html,body{width:1200px;height:900px;overflow:hidden;background:var(--stage)}
  .stage{position:relative;width:1200px;height:900px}

  .backing-sheet{position:absolute;left:258px;top:192px;width:408px;height:578px;background:var(--orange)}

  .letterhead{position:absolute;left:324px;top:126px;width:410px;height:580px;background:var(--paper);font-family:"Open Sans",sans-serif}
  .brand-mark{position:absolute;display:flex;flex-direction:column;align-items:center;gap:10px}
  .brand-mark .square{width:38px;height:38px;background:var(--brand)}
  .brand-name{font-family:"Josefin Sans",sans-serif;font-weight:600;color:var(--brand);letter-spacing:.14em;white-space:nowrap}
  .letterhead .brand-mark{left:29px;top:30px;width:114px}
  .letterhead .brand-name{font-size:11px}

  .contact-block{position:absolute;right:36px;top:34px;text-align:right;font-size:8px;line-height:10.5px;color:var(--muted);padding-right:9px;border-right:1px solid var(--rule)}
  .fold-mark{position:absolute;left:0;width:10px;height:1px;background:var(--rule)}
  .fold-mark.top{top:193px}
  .fold-mark.mid{top:386px}

  .letter-body{position:absolute;left:46px;top:177px;width:337px;font-family:"Arimo",sans-serif;font-size:7.9px;line-height:9.6px;color:var(--ink);text-align:justify}
  .letter-body p{margin-bottom:9.6px}

  .signature{position:absolute;left:46px;top:450px;width:78px;height:24px;background:linear-gradient(90deg,rgba(35,48,122,.18),rgba(35,48,122,.05))}
  .signer{position:absolute;left:46px;top:479px;font-size:8px;color:var(--ink)}

  .site{position:absolute;left:48px;top:560px;font-size:8px;letter-spacing:.16em;color:var(--muted)}
  .footer-bar{position:absolute;left:30px;bottom:0;width:112px;height:5px;background:var(--orange)}

  .card{position:absolute;left:782px;width:173px;height:99px}
  .card-front{top:319px;background:linear-gradient(135deg,var(--orange),var(--orange-deep))}
  .card-front .brand-mark{left:0;right:0;top:26px;gap:9px}
  .card-front .square{width:30px;height:30px;background:#f5c53a}
  .card-front .brand-name{font-size:6.5px;color:#f5c53a}
  .card-front .card-site{position:absolute;left:0;right:0;top:84px;text-align:center;font-size:4.5px;letter-spacing:.12em;color:#fde1c0}

  .card-back{top:463px;background:var(--paper);font-family:"Open Sans",sans-serif}
  .card-back .brand-mark{left:10px;top:13px;width:70px;gap:6px}
  .card-back .square{width:22px;height:22px}
  .card-back .brand-name{font-size:5.8px}
  .holder{position:absolute;right:11px;top:42px;text-align:right;padding-right:6px;border-right:3px solid var(--brand)}
  .holder-name{font-size:6px;font-weight:600;color:var(--brand);line-height:7px}
  .holder-title{font-size:3.6px;color:var(--muted);line-height:5px}
  .card-contacts{position:absolute;right:13px;top:70px;text-align:right;font-size:3.8px;line-height:5.2px;color:var(--muted);padding-right:4px;border-right:1px solid var(--rule)}
</style>
</head>
<body>
<main class="stage">
  <div class="backing-sheet"></div>

  <article class="letterhead">
    <div class="brand-mark">
      <span class="square"></span>
      <span class="brand-name">BRIGHT ELM HOLDINGS</span>
    </div>
    <address class="contact-block">
      +7 000 555 0142<br>
      ddavis@brightelmholdings.fund<br>
      Moscow, Vetrova str, 7, office 4
    </address>
    <span class="fold-mark top"></span>
    <span class="fold-mark mid"></span>

    <div class="letter-body">
      <p>Lorem ipsum dolor sit amet, consectetur adipisicing elit, sed do eiusmod tempor incididunt ut labore et dolore magna aliqua. Ut enim ad minim veniam, quis nostrud exercitation ullamco laboris nisi ut aliquip ex ea commodo consequat.</p>
      <p>Duis aute irure dolor in reprehenderit in voluptate velit esse cillum dolore eu fugiat nulla pariatur. Excepteur sint occaecat cupidatat non proident, sunt in culpa qui officia deserunt mollit anim id est laborum.</p>
      <p>Sed ut perspiciatis unde omnis iste natus error sit voluptatem accusantium doloremque laudantium, totam rem aperiam, eaque ipsa quae ab illo inventore veritatis et quasi architecto beatae vitae dicta sunt explicabo.</p>
      <p>Nemo enim ipsam voluptatem quia voluptas sit aspernatur aut odit aut fugit, sed quia consequuntur magni dolores eos qui ratione voluptatem sequi nesciunt. Neque porro quisquam est, qui dolorem ipsum quia dolor sit amet, consectetur, adipisci velit, sed quia non numquam eius modi tempora incidunt ut labore et dolore magnam aliquam quaerat voluptatem.</p>
      <p>Ut enim ad minima veniam, quis nostrum exercitationem ullam corporis suscipit laboriosam, nisi ut aliquid ex ea commodi consequatur?</p>
      <p>Quis autem vel eum iure reprehenderit qui in ea voluptate velit esse quam nihil molestiae consequatur, vel illum qui dolorem eum fugiat quo voluptas nulla pariatur?</p>
      <p>Duis aute irure dolor in reprehenderit in voluptate velit esse cillum dolore eu fugiat nulla pariatur. Excepteur sint occaecat cupidatat non proident, sunt in culpa qui officia deserunt mollit anim id est laborum.</p>
    </div>

    <div class="signature" role="img" aria-label="Handwritten signature of Daniel Davis in blue ink"></div>
    <p class="signer">Daniel Davis</p>

    <p class="site">brightelmholdings.fund</p>
    <span class="footer-bar"></span>
  </article>

  <section class="card card-front">
    <div class="brand-mark">
      <span class="square"></span>
      <span class="brand-name">BRIGHT ELM HOLDINGS</span>
    </div>
    <p class="card-site">brightelmholdings.fund</p>
  </section>

  <section class="card card-back">
    <div class="brand-mark">
      <span class="square"></span>
      <span class="brand-name">BRIGHT ELM HOLDINGS</span>
    </div>
    <div class="holder">
      <p class="holder-name">Daniel Davis</p>
      <p class="holder-title">Certified Public Accountant</p>
    </div>
    <address class="card-contacts">
      +7 000 555 0142<br>
      ddavis@brightelmholdings.fund<br>
      Moscow, Vetrova str, 7, office 4
    </address>
  </section>
</main>
</body>
</html>
```